Brightwell Homes Guide Business card

I have had at the logo designed here and attached. The business compares off the plan apartments in Sydney and provides quick comparison for new home buyers e.g price, floor plans and location. I would like the complimentary colours used on the business card. I would like it be unique but also look professional. I also have a website to gain inspiration from www.brightwellhomesguide.com.au
Updates
Industry/Entity Type
Business
Contact Information for Business Card
Helen Vostrakis
Director of Business Development
e: helen.vostrakis@brightwellhomesguide.com.au
p: (02) 8143 7692
m: 0431 572 908
w: www.brightwellhomesguide.com.au
Look and feel
Each slider illustrates characteristics of the customer's brand and the style your logo design should communicate.

```html
<!DOCTYPE html>
<html lang="en">
<head>
<meta charset="utf-8">
<title>Brightwell Homes Guide – Business Card</title>
<link href="https://fonts.googleapis.com/css2?family=Open+Sans:wght@400;600;700&display=swap" rel="stylesheet">
<style>
  :root {
    --page-bg: #e9eaeb;
    --card-bg: #fbfbfb;
    --card-edge: #d8dadc;
    --brand-green: #5a9e32;
    --brand-blue: #1f63a8;
    --ink: #1d1d1d;
    --icon: #1f5a96;
    --mark-tint: rgba(31, 99, 168, 0.08);
  }
  * { margin: 0; padding: 0; box-sizing: border-box; }
  html, body {
    width: 1200px; height: 970px; overflow: hidden;
    background: var(--page-bg);
    font-family: "Open Sans", Arial, sans-serif;
  }
  .card {
    position: absolute; left: 100px; top: 207px;
    width: 1000px; height: 556px;
    background: var(--card-bg);
    border: 1px solid var(--card-edge);
    box-shadow: 0 10px 30px rgba(0,0,0,0.12);
    overflow: hidden;
  }
  .brand {
    position: absolute; left: 48px; top: 78px;
    display: flex; align-items: center; gap: 16px;
  }
  .brand-square { width: 58px; height: 58px; background: var(--brand-blue); }
  .brand-name {
    font-size: 40px; font-weight: 600; color: var(--brand-green);
    letter-spacing: -0.5px;
  }
  .brand-mark-faint {
    position: absolute; left: 579px; top: 171px;
    width: 332px; height: 313px; background: var(--mark-tint);
  }
  .person { position: absolute; left: 50px; top: 260px; }
  .person-name {
    font-size: 28px; font-weight: 700; color: var(--brand-blue);
    text-transform: uppercase; letter-spacing: 0.3px; line-height: 1.2;
  }
  .person-role { font-size: 22px; color: var(--ink); margin-top: 4px; }
  .contacts { position: absolute; left: 50px; top: 356px; list-style: none; }
  .contacts li {
    display: flex; align-items: center; gap: 12px;
    height: 33.5px; font-size: 21px; color: var(--ink); white-space: nowrap;
  }
  .contacts svg { width: 20px; height: 20px; flex: none; fill: var(--icon); }
  .address {
    position: absolute; left: 620px; top: 355px;
    font-size: 22px; line-height: 31px; color: var(--ink); font-style: normal;
  }
  .band { position: absolute; bottom: 0; height: 36px; }
  .band-green { left: 0; width: 529px; background: var(--brand-green); }
  .band-blue { left: 538px; right: 0; background: var(--brand-blue); }
</style>
</head>
<body>
  <div class="card">
    <div class="brand">
      <div class="brand-square"></div>
      <span class="brand-name">Brightwell Homes Guide</span>
    </div>
    <div class="brand-mark-faint"></div>

    <div class="person">
      <div class="person-name">Helen Vostrakis</div>
      <div class="person-role">Director of Business Development</div>
    </div>

    <ul class="contacts">
      <li>
        <svg viewBox="0 0 20 20" aria-hidden="true"><rect x="5" y="1" width="10" height="18" rx="2"/><rect x="7" y="4" width="6" height="8" fill="#fff"/></svg>
        0431 572 908
      </li>
      <li>
        <svg viewBox="0 0 20 20" aria-hidden="true"><path d="M2 8c0-3 4-5 8-5s8 2 8 5l-4 1-1-2H7L6 9z"/><path d="M4 11h12l1 6H3z"/></svg>
        (02) 8143 7692
      </li>
      <li>
        <svg viewBox="0 0 20 20" aria-hidden="true"><rect x="1" y="4" width="18" height="12"/><path d="M1 4l9 7 9-7" fill="none" stroke="#fff" stroke-width="1.6"/></svg>
        helen.vostrakis@brightwellhomesguide.com.au
      </li>
      <li>
        <svg viewBox="0 0 20 20" aria-hidden="true"><circle cx="10" cy="10" r="9"/><path d="M1 10h18M10 1v18M10 1c-4 4-4 14 0 18M10 1c4 4 4 14 0 18" fill="none" stroke="#fff" stroke-width="1.2"/></svg>
        www.brightwellhomesguide.com.au
      </li>
    </ul>

    <address class="address">
      Level 18, Harbourline Tower 2<br>
      Kent Street Sydney,<br>
      NSW 2000
    </address>

    <div class="band band-green"></div>
    <div class="band band-blue"></div>
  </div>
</body>
</html>
```